Clone http://www.pebbledeskwriter.com/ (fully functioning WordPress website - not just design)

1) Clone or recreate http://www.pebbledeskwriter.com/ in Wordpress with WooCommerece plugin
2) Connect to our Existing Quendo Account
3) Make site-wide text only changes that we provide you when site is complete.

We will provide all the graphics according to your size requirements.

Cash awarded to the closest copy of http://www.pebbledeskwriter.com/

Target Market(s)

WordPress developer

Number of Pages Required

5+ page

Font styles to use
Sans Serif

Colors
abd037
cadf82
eaf2ce

Requirements
Must have
• Fully functioning website.

```html
<!DOCTYPE html>
<html lang="en">
<head>
<meta charset="utf-8">
<title>Pebbledesk Writer – Mail Merge Online</title>
<link rel="stylesheet" href="https://fonts.googleapis.com/css2?family=Mulish:wght@300;400;600;700;800&display=swap">
<style>
  :root {
    --green: #abd037;
    --green-mid: #cadf82;
    --green-pale: #eaf2ce;
    --ink: #1d1d1b;
    --body: #3a3a3a;
    --muted: #8f8f8f;
    --footer: #0b0b0b;
    --white: #ffffff;
  }
  * { margin: 0; padding: 0; box-sizing: border-box; }
  html, body { width: 725px; height: 1200px; overflow: hidden; }
  body { position: relative; background: var(--white); font-family: "Mulish", Arial, sans-serif; color: var(--body); }
  .abs { position: absolute; }

  .top-bar { left: 0; top: 0; width: 725px; height: 38px; background: var(--green); }
  .account-links { right: 30px; top: 15px; display: flex; gap: 13px; align-items: center; font-size: 7px; font-weight: 700; color: var(--white); letter-spacing: .3px; }
  .menu-icon { width: 8px; height: 6px; border-top: 1px solid #fff; border-bottom: 1px solid #fff; position: relative; }
  .menu-icon::after { content: ""; position: absolute; left: 0; top: 1.5px; width: 8px; border-top: 1px solid #fff; }

  .hero { left: 0; top: 38px; width: 725px; height: 360px; overflow: hidden; }
  .hero-photo { position: absolute; inset: 0; background: linear-gradient(100deg, #c9cccb 0%, #e8e6e2 30%, #efeeec 55%, #b9b3bc 78%, #7a7488 100%); }
  .hero-veil { position: absolute; inset: 0; background: radial-gradient(ellipse at 50% 45%, rgba(255,255,255,.8), rgba(255,255,255,.35) 70%); }

  .brand { left: 94px; top: 58px; display: flex; align-items: center; gap: 5px; font-size: 13px; font-weight: 800; color: var(--green); }
  .brand-dot { width: 10px; height: 10px; border-radius: 50%; background: var(--green); }

  .main-nav { left: 424px; top: 54px; display: flex; gap: 12px; font-size: 7.5px; font-weight: 600; color: var(--ink); }
  .main-nav a { color: inherit; text-decoration: none; padding-bottom: 3px; }
  .main-nav a.active { border-bottom: 2px solid var(--green); }

  .hero-title { left: 0; top: 145px; width: 725px; text-align: center; font-size: 25px; font-weight: 800; line-height: 37px; color: var(--ink); text-transform: uppercase; letter-spacing: .2px; }
  .hero-lead { left: 0; top: 231px; width: 725px; text-align: center; font-size: 9.2px; line-height: 15px; color: var(--ink); }
  .btn { display: flex; align-items: center; justify-content: center; background: var(--green); color: var(--white); font-weight: 700; text-transform: uppercase; }
  .hero-cta { left: 298px; top: 307px; width: 128px; height: 30px; font-size: 10.5px; letter-spacing: .3px; }
  .hero-note { left: 0; top: 344px; width: 725px; text-align: center; font-size: 9.5px; color: var(--ink); }

  .section-title { left: 0; top: 436px; width: 725px; text-align: center; font-size: 18.5px; font-weight: 400; color: var(--ink); }

  .steps { left: 86px; top: 495px; width: 550px; display: flex; justify-content: space-between; }
  .step { width: 182px; text-align: center; }
  .step-icon { width: 48px; height: 48px; margin: 0 auto; border: 1.3px solid var(--ink); border-radius: 50%; display: flex; align-items: center; justify-content: center; }
  .step-title { margin-top: 10px; font-size: 7.8px; font-weight: 700; color: var(--ink); letter-spacing: .5px; }
  .step-rule { width: 60px; margin: 4px auto 6px; border-top: 1.2px solid var(--green-mid); }
  .step-text { font-size: 7px; line-height: 11.5px; color: var(--muted); font-weight: 300; white-space: nowrap; }

  .pdf-button { left: 301px; top: 634px; width: 123px; height: 28px; background: #e2e2e2; border: 1px solid #cfcfcf; display: flex; align-items: center; gap: 8px; padding-left: 15px; font-size: 7.5px; color: var(--ink); }

  .phone { left: 88px; top: 742px; width: 244px; height: 370px; border: 3px solid #e3e3e3; border-bottom: none; border-radius: 36px 36px 0 0; background: var(--white); box-shadow: -6px 4px 0 #f3f3f3; }
  .phone-camera { left: 122px; top: 20px; width: 8px; height: 8px; border-radius: 50%; background: #dadada; }
  .phone-speaker { left: 95px; top: 37px; width: 42px; height: 6px; border: 1.5px solid #d5d5d5; border-radius: 4px; }
  .phone-sensor { left: 80px; top: 38px; width: 4px; height: 4px; border-radius: 50%; background: #d5d5d5; }
  .phone-screen { left: 23px; top: 65px; width: 202px; height: 285px; background: linear-gradient(120deg, #7f9aa8 0%, #93aab4 50%, #d9cbb8 80%, #f0e4d6 100%); }

  .tour { left: 385px; top: 772px; width: 240px; }
  .tour-title { font-size: 8px; font-weight: 700; color: var(--ink); letter-spacing: .4px; }
  .tour-rule { width: 40px; margin: 4px 0 8px; border-top: 1.2px solid var(--green-mid); }
  .tour-text { font-size: 6.8px; line-height: 11.7px; color: var(--muted); font-weight: 300; margin-bottom: 11.7px; white-space: nowrap; }
  .tour-note { left: 385px; top: 945px; font-size: 10.5px; color: var(--ink); }
  .tour-cta { left: 385px; top: 970px; width: 126px; height: 31px; font-size: 8px; }

  .site-footer { left: 0; top: 1092px; width: 725px; height: 108px; background: var(--footer); }
  .footer-links { left: 0; top: 1117px; width: 725px; display: flex; justify-content: center; gap: 14px; font-size: 5.5px; color: #cfcfcf; }
  .social { left: 0; top: 1137px; width: 725px; display: flex; justify-content: center; gap: 5px; }
  .social span { width: 10px; height: 10px; border-radius: 50%; background: #bdbdbd; }
  .copyright { left: 0; top: 1177px; width: 725px; text-align: center; font-size: 4.5px; color: #6a6a6a; }
</style>
</head>
<body>
  <div class="abs top-bar"></div>
  <div class="abs account-links"><span>LOG IN</span><span>SIGN UP</span><span class="menu-icon"></span></div>

  <div class="abs hero">
    <div class="hero-photo" role="img" aria-label="Person typing on a laptop at a bright desk"></div>
    <div class="hero-veil"></div>
  </div>

  <div class="abs brand"><span class="brand-dot"></span>Pebbledesk</div>
  <nav class="abs main-nav">
    <a class="active">HOME</a><a>TOUR</a><a>PRICE</a><a>OUR TEAM</a><a>CONTACT US</a>
  </nav>

  <h1 class="abs hero-title">Do you have a letter you need<br>to send out to multiple people?</h1>
  <p class="abs hero-lead">Mail merge is the automatic addition of names and addresses from a spreadsheet to letters<br>and envelopes in order to facilitate sending personalised mail to many people.</p>
  <div class="abs btn hero-cta">Start a free trail</div>
  <p class="abs hero-note">Start building your mail merge online now!</p>

  <h2 class="abs section-title">100% Easier Than Using Quillpad!</h2>

  <div class="abs steps">
    <div class="step">
      <div class="step-icon">
        <svg width="26" height="22" viewBox="0 0 26 22" fill="none" stroke="#abd037" stroke-width="1.6" stroke-linecap="round" stroke-linejoin="round">
          <path d="M7 16H6a5 5 0 0 1 0-10 7 7 0 0 1 13 1h1a4.5 4.5 0 0 1 0 9h-2"/><path d="M13 20v-9M9.5 14l3.5-3.5 3.5 3.5"/>
        </svg>
      </div>
      <div class="step-title">UPLOAD YOUR DATA</div><div class="step-rule"></div>
      <p class="step-text">Lorem ipsum dolor sit amet, consectetur adipisc<br>Pellentesque vel enim a elit viverra elementum.<br>Aliquam erat volutpat.</p>
    </div>
    <div class="step">
      <div class="step-icon">
        <svg width="24" height="24" viewBox="0 0 24 24" fill="none" stroke="#abd037" stroke-width="1.6" stroke-linejoin="round">
          <path d="M4 20l2-6L17 3l4 4-11 11z"/><path d="M14 6l4 4M4 20l6-2"/>
        </svg>
      </div>
      <div class="step-title">DESIGN YOUR TEMPLATE</div><div class="step-rule"></div>
      <p class="step-text">Lorem ipsum dolor sit amet, consectetur adipisc<br>Pellentesque vel enim a elit viverra elementum.<br>Aliquam erat volutpat.</p>
    </div>
    <div class="step">
      <div class="step-icon">
        <svg width="20" height="24" viewBox="0 0 20 24" fill="none" stroke="#abd037" stroke-width="1.6" stroke-linejoin="round">
          <path d="M2 2h11l5 5v15H2z"/><path d="M6 11h8M6 14.5h8M6 18h8"/>
        </svg>
      </div>
      <div class="step-title">MERGE TO PDF</div><div class="step-rule"></div>
      <p class="step-text">Lorem ipsum dolor sit amet, consectetur adipisc<br>Pellentesque vel enim a elit viverra elementum.<br>Aliquam erat volutpat.</p>
    </div>
  </div>

  <div class="abs pdf-button">
    <svg width="16" height="19" viewBox="0 0 16 19"><path d="M1 1h10l4 4v13H1z" fill="#fff" stroke="#333"/><rect x="0" y="9" width="13" height="6" fill="#333"/><text x="1.5" y="14" font-size="4.5" font-family="Arial, sans-serif" font-weight="700" fill="#fff">PDF</text></svg>
    Click to view the PDF
  </div>

  <div class="abs phone">
    <div class="abs phone-camera"></div>
    <div class="abs phone-sensor"></div>
    <div class="abs phone-speaker"></div>
    <div class="abs phone-screen" role="img" aria-label="Surprised woman in glasses in front of a wall of drawn envelopes"></div>
  </div>

  <div class="abs tour">
    <div class="tour-title">TRAIL A FREE TOUR</div><div class="tour-rule"></div>
    <p class="tour-text">Lorem Ipsum is simply dummy text of the printing and typesetting<br>industry. Lorem Ipsum has been the industry's standard dummy text<br>ever since the 1500s, when an unknown printer took a galley of type<br>and scrambled it to make a type specimen book. It has survived not.</p>
    <p class="tour-text">But also the leap into electronic typesetting, remaining essentially<br>It was popularised in the 1960s with the release of Transfera sheets.</p>
    <p class="tour-text">It is a long established fact that a reader will be distracted by the .<br>of a page when looking at its layout. The point of using Lorem Ipsum.</p>
  </div>
  <p class="abs tour-note">Start building your mail merge online now!</p>
  <div class="abs btn tour-cta">Start a free trail</div>

  <footer class="abs site-footer"></footer>
  <div class="abs footer-links"><span>Browse</span><span>Privacy Policy</span><span>Terms &amp; Conditions</span><span>Refund Policy</span></div>
  <div class="abs social"><span></span><span></span><span></span></div>
  <p class="abs copyright">© Copyright 2017 Lanthorn Technologies. All Rights Reserved</p>
</body>
</html>
```